Book jacket for Drumlore

We need a book jacket design (hard cover front, back, spine, flaps; soft cover and eBook). for a social psychology book with the general cluelessness (being "out of it") of how people function both in their personal and social lives. This is the third book written by the author, a practicing psychiatrist, and the content centers on a single subject, people's lack of genuine emotional contact, their cluelessness with themselves and with current national and world events.

Target Market(s)

People who want to better understand the state the nation and world is in now, and what they can do about it.

Font styles to use
Serif
Sans Serif

Requirements
Must have
• Bold, eye-catching cover
Nice to have
• Like the idea of separating the title word (drum lore) to better emphasize the concept of lack of contact

```html
<!DOCTYPE html>
<html lang="en">
<head>
<meta charset="utf-8">
<title>Drumlore — Book Cover</title>
<link rel="stylesheet" href="https://fonts.googleapis.com/css2?family=Jost:wght@400&family=Oswald:wght@700&display=swap">
<style>
  :root {
    --cover-grey-dark: #6c6d71;
    --cover-grey-light: #86878a;
    --block-deep: #a3292f;
    --block-bright: #e83a41;
    --letter-white: #f7f7f7;
    --author-white: #ffffff;
    --shadow: #3e3f42;
  }
  html, body {
    margin: 0;
    padding: 0;
    width: 1000px;
    height: 1200px;
    overflow: hidden;
  }
  .book-cover {
    position: relative;
    width: 1000px;
    height: 1200px;
    background: linear-gradient(90deg, var(--cover-grey-dark) 0%, var(--cover-grey-light) 100%);
    overflow: hidden;
  }
  .author-name {
    position: absolute;
    top: 150px;
    left: 0;
    width: 100%;
    margin: 0;
    text-align: center;
    font-family: "Jost", "Helvetica Neue", Arial, sans-serif;
    font-weight: 400;
    font-size: 34px;
    letter-spacing: 4px;
    color: var(--author-white);
  }
  .title-art {
    position: absolute;
    top: 0;
    left: 0;
    width: 1000px;
    height: 1200px;
  }
  .title-word {
    font-family: "Oswald", "Arial Narrow", sans-serif;
    font-weight: 700;
    font-size: 300px;
    fill: var(--letter-white);
  }
</style>
</head>
<body>
  <main class="book-cover">
    <p class="author-name">HAROLD VENN M.D.</p>

    <svg class="title-art" viewBox="0 0 1000 1200">
      <title>Drumlore</title>
      <defs>
        <filter id="floor-shadow-blur" x="-50%" y="-200%" width="200%" height="500%">
          <feGaussianBlur stdDeviation="18"/>
        </filter>
      </defs>

      <ellipse class="floor-shadow" cx="500" cy="1100" rx="290" ry="24" fill="var(--shadow)" opacity="0.5" filter="url(#floor-shadow-blur)"/>

      <g class="title-upper">
        <rect x="190" y="340" width="620" height="310" fill="var(--block-deep)"/>
        <text class="title-word" x="500" y="610" text-anchor="middle" textLength="520" lengthAdjust="spacingAndGlyphs">DRUM</text>
      </g>

      <g class="title-lower">
        <rect x="190" y="680" width="620" height="310" fill="var(--block-bright)"/>
        <text class="title-word" x="500" y="950" text-anchor="middle" textLength="520" lengthAdjust="spacingAndGlyphs">LORE</text>
      </g>
    </svg>
  </main>
</body>
</html>
```